Custom Home Page for our new Website

We need a custom home page designed for our new website. We are a successful local copier dealer who is rebuilding our website from scratch. We have decided on Wordpress as our CMS platform and have purchased the professional Corvel theme.

The custom homepage we want will be an imitation of the screen on latest model of copiers we carry. (A picture of this is attached.) the goal is to imitate this style while creating a unique, user-friendly, helpful portal to our website.

The winning entry will make the best transition between the menu structure of our current website (www.hlumo.net) and the new layout.

Target Market(s)

Our target market is small to medium sized businesses in the Southeast US. The users of our site are generally IT professionals looking for drivers/support, gatekeepers or other support staff placing service calls and supply orders or prospects looking for information about our company and products.

Requirements
Must have
• Clean design, no distracting elements
• Modern aesthetic
• A color palette that can be used as a basis for the Skin for the rest of the site (The site's look will be based on the winning homepage design.)
• Simple navigation
• Easy to read
• Easily viewed on both desktop and tablet sized screens
• Our logo
• Easily update-able
• Maximum of 4 of the large squares

```html
<!DOCTYPE html>
<html lang="en">
<head>
<meta charset="utf-8">
<title>Norvale – Business Copiers</title>
<link href="https://fonts.googleapis.com/css2?family=Oswald:wght@400;500&family=Open+Sans:wght@400;600;700&display=swap" rel="stylesheet">
<style>
  :root {
    --red-deep: #4a0f12;
    --red-mid: #7a1a1f;
    --red-bright: #b52b30;
    --red-button: #d81e22;
    --black: #050505;
    --white: #ffffff;
    --grey-text: #b9b4b4;
    --rule: #2a2a2a;
  }
  * { margin: 0; padding: 0; box-sizing: border-box; }
  html, body { width: 1200px; height: 730px; overflow: hidden; background: var(--black); }
  .page {
    position: relative; width: 1200px; height: 730px; overflow: hidden;
    background: linear-gradient(100deg, var(--red-bright) 0%, var(--red-mid) 35%, var(--red-deep) 75%, #2a0709 100%);
    font-family: "Open Sans", sans-serif; color: var(--white);
  }
  .backdrop { position: absolute; inset: 0; }
  .site-header {
    position: absolute; left: 0; top: 0; width: 1200px; height: 114px;
    background: linear-gradient(180deg, #4b1014 0%, #5a1419 100%);
    border-bottom: 3px solid #1a0406;
  }
  .brand {
    position: absolute; left: 162px; top: 36px;
    display: flex; align-items: center; gap: 12px;
    font-family: "Oswald", sans-serif; font-weight: 500; font-size: 38px;
    letter-spacing: 1px; color: var(--white);
  }
  .brand-dot { width: 22px; height: 22px; border-radius: 50%; background: var(--red-button); }
  .branches {
    position: absolute; right: 129px; top: 14px; text-align: right;
    font-weight: 700; font-size: 14px; line-height: 19px; color: var(--grey-text);
  }
  .main-nav { position: absolute; right: 129px; top: 78px; display: flex; gap: 27px; }
  .main-nav a {
    position: relative; font-family: "Oswald", sans-serif; font-size: 18px;
    color: var(--white); text-decoration: none; padding: 0 0 15px;
  }
  .main-nav a.is-current::after {
    content: ""; position: absolute; left: -12px; right: -12px; bottom: 0; height: 3px; background: var(--red-button);
  }
  .hero-title {
    position: absolute; left: 158px; top: 148px;
    font-family: "Oswald", sans-serif; font-weight: 400; font-size: 64px; line-height: 70px;
    text-shadow: 1px 2px 3px rgba(0,0,0,.35);
  }
  .hero-text {
    position: absolute; left: 164px; top: 306px; width: 345px;
    font-size: 11.5px; line-height: 17px;
  }
  .read-more {
    position: absolute; left: 160px; top: 409px; width: 241px; height: 65px;
    border-radius: 7px; border: 3px solid #e35a5d;
    background: linear-gradient(180deg, #ee4a4c 0%, var(--red-button) 50%, #b8151a 100%);
    font-size: 28px; font-weight: 400; letter-spacing: .5px;
    display: flex; align-items: center; justify-content: center;
    color: var(--white); text-decoration: none; text-shadow: 0 1px 2px rgba(0,0,0,.4);
  }
  .product-visual {
    position: absolute; left: 655px; top: 145px; width: 395px; height: 347px;
    background: linear-gradient(180deg, #e4e4e4 0%, #cfcfcf 60%, #a9a9a9 100%);
    border-radius: 4px;
  }
  .slider-dots { position: absolute; left: 590px; top: 504px; display: flex; gap: 6px; }
  .slider-dots span { width: 11px; height: 11px; border-radius: 50%; background: #8a8a8a; }
  .slider-dots span.is-active { background: var(--white); }
  .portal-links {
    position: absolute; left: 0; top: 570px; width: 1200px; height: 100px;
  }
  .portal-link {
    position: absolute; top: 0; width: 180px; margin-left: -90px;
    text-align: center; text-decoration: none; color: var(--white);
    font-family: "Oswald", sans-serif; font-size: 19px;
  }
  .portal-icon { height: 62px; display: flex; align-items: flex-end; justify-content: center; margin-bottom: 6px; }
  .icon-circle { width: 48px; height: 48px; border-radius: 50%; background: var(--white); }
  .icon-visual { width: 64px; height: 54px; background: linear-gradient(180deg, #e8e8e8, #9c9c9c); }
  .icon-support { width: 38px; height: 52px; background: linear-gradient(180deg, #ffffff, #d9d9d9); border-radius: 18px 18px 6px 6px; }
  .site-footer {
    position: absolute; left: 130px; top: 694px; width: 940px;
    border-top: 1px solid var(--rule); padding-top: 10px; text-align: right;
    font-size: 11px; color: #cfcfcf; padding-right: 8px;
  }
</style>
</head>
<body>
<div class="page">
  <svg class="backdrop" width="1200" height="730" viewBox="0 0 1200 730" aria-hidden="true">
    <polygon points="0,114 420,114 130,730 0,730" fill="#ffffff" opacity="0.04"/>
    <polygon points="820,114 1200,114 1200,470" fill="#000000" opacity="0.18"/>
    <polygon points="1050,114 1200,114 1200,730 960,730" fill="#000000" opacity="0.2"/>
    <rect x="0" y="498" width="1200" height="232" fill="#000000" opacity="0.25"/>
    <path d="M0,730 L0,640 Q600,430 1200,640 L1200,730 Z" fill="#050505"/>
    <path d="M60,730 Q250,560 600,535 Q950,560 1140,730 Z" fill="#000000"/>
  </svg>

  <header class="site-header">
    <div class="brand"><span class="brand-dot"></span>NORVALE</div>
    <div class="branches">
      <div>FAIRMONT 555.201.4410</div>
      <div>ASHBURY&nbsp; 555.308.7720</div>
    </div>
    <nav class="main-nav">
      <a href="#" class="is-current">HOME</a>
      <a href="#">WHO WE ARE</a>
      <a href="#">WHAT WE OFFER</a>
      <a href="#">SUPPORT</a>
      <a href="#">CONTACTUS</a>
    </nav>
  </header>

  <h1 class="hero-title">Business<br>Copiers/MFPs</h1>
  <p class="hero-text">The new Kestrel user interface lets you edit your documents, drag and rearrange files all with the slide of a finger. The 10.1" color LCD touch control panel is customizable to meet virtually all of your needs.</p>
  <a href="#" class="read-more">READ MORE</a>

  <div class="product-visual" role="img" aria-label="Photo of a white multifunction office copier with finisher and paper tray"></div>

  <div class="slider-dots"><span class="is-active"></span><span></span></div>

  <div class="portal-links">
    <a href="#" class="portal-link" style="left:240px">
      <div class="portal-icon"><span class="icon-circle"></span></div>WHO ARE WE
    </a>
    <a href="#" class="portal-link" style="left:485px">
      <div class="portal-icon"><span class="icon-visual" role="img" aria-label="Small copier icon"></span></div>WHAT WE OFFER
    </a>
    <a href="#" class="portal-link" style="left:718px">
      <div class="portal-icon"><span class="icon-support" role="img" aria-label="Support agent with headset icon"></span></div>SUPPORT
    </a>
    <a href="#" class="portal-link" style="left:956px">
      <div class="portal-icon">
        <svg width="34" height="44" viewBox="0 0 34 44" aria-hidden="true">
          <path d="M8 2 L14 12 Q15 14 13 16 L10 19 Q13 28 21 34 L24 31 Q26 29 28 31 L33 38 Q34 40 32 42 L28 44 Q12 40 3 20 Q0 12 3 5 L5 2 Q7 0 8 2 Z" fill="#ffffff"/>
        </svg>
      </div>CONTACT US
    </a>
  </div>

  <footer class="site-footer">Copyrights 2013, All rights reserved by Norvale, Inc.</footer>
</div>
</body>
</html>
```